R7M Meridian Business Card Design

We need a business card created for our New Business "R7M Meridian"<br/><br/>The business card design is up to you however the following information must be on the business card:<br/><br/>Front of the business card -<br/>Email :dorianv@r7mmeridian.nz<br/>Mobile: +64 (0) 22 4871 659<br/>Website: www.r7mmeridian.nz<br/>Card Owner Name: Dorian Valcourt<br/>Company Title: Business Development Manager<br/>Slogan: "Crafted for every occasion". <br/>Logo On the front attached to the design brief<br/><br/>On the back: <br/>Space on the back for 4 more versions of the logo across the bottom of the card indicating different subsidiary brands - R7M Coffee, R7M Arts, R7M ?? (The card will be used for all of these brands - We Will add the extra subsidiary logos to the design once the design is finished (We are a graphics design team). <br/><br/>Other than that we want a premium feeling logo that remains universally usable depending on the business entity that we are using the card for. The use of bright bold colours would be great but we still want the card to feel premium.
Target Market(s)
Gift Design and Manufacturing Companies
Contact Information for Business Card
Front of the business card -
Email :dorianv@r7mmeridian.nz
Mobile: +64 (0) 22 4871 659
Website: www.r7mmeridian.nz
Card Owner Name: Dorian Valcourt
Company Title: Business Development Manager
Slogan: "Crafted for every occasion".
Logo On the front attached to the design brief

```html
<!DOCTYPE html>
<html lang="en">
<head>
<meta charset="utf-8">
<title>R7M Meridian Business Card</title>
<link href="https://fonts.googleapis.com/css2?family=Lato:wght@400;700;900&display=swap" rel="stylesheet">
<style>
  :root {
    --brand-blue: #2a3b97;
    --card-white: #f3f3f3;
    --ink-dark: #222326;
    --page-bg: #e4ddc9;
    --text-light: #ffffff;
  }
  * { margin: 0; padding: 0; box-sizing: border-box; }
  html, body { width: 1200px; height: 960px; overflow: hidden; }
  body {
    background: var(--page-bg);
    font-family: "Lato", Arial, sans-serif;
    position: relative;
  }
  .card {
    position: absolute;
    left: 290px;
    width: 620px;
    height: 354px;
    border-radius: 4px;
    box-shadow: 0 10px 24px rgba(60, 50, 30, 0.18);
  }
  .card-back { top: 96px; background: var(--brand-blue); }
  .card-front { top: 510px; background: var(--card-white); }

  .brand-name {
    position: absolute;
    font-weight: 900;
    letter-spacing: 0.5px;
    white-space: nowrap;
  }
  .card-back .brand-name {
    color: var(--text-light);
    font-size: 44px;
    left: 50%;
    top: 120px;
    transform: translateX(-50%);
  }
  .slogan {
    position: absolute;
    right: 148px;
    top: 212px;
    color: var(--text-light);
    font-size: 14px;
    letter-spacing: 0.4px;
  }

  .card-front .brand-name {
    color: var(--brand-blue);
    font-size: 30px;
    left: 48px;
    top: 156px;
  }
  .divider {
    position: absolute;
    left: 300px;
    top: 110px;
    width: 2px;
    height: 130px;
    background: var(--brand-blue);
  }
  .contact-block {
    position: absolute;
    left: 326px;
    top: 110px;
  }
  .owner-name {
    color: var(--brand-blue);
    font-weight: 900;
    font-size: 22px;
    line-height: 1.1;
  }
  .owner-title {
    color: var(--ink-dark);
    font-size: 12.5px;
    margin: 3px 0 18px;
  }
  .contact-list { list-style: none; }
  .contact-item {
    display: flex;
    align-items: center;
    gap: 10px;
    color: var(--ink-dark);
    font-size: 13px;
    line-height: 22px;
  }
  .contact-icon { width: 13px; height: 13px; flex: none; }
</style>
</head>
<body>
  <section class="card card-back">
    <div class="brand-name">R7M Meridian</div>
    <p class="slogan">Crafted for every occasion</p>
  </section>

  <section class="card card-front">
    <div class="brand-name">R7M Meridian</div>
    <div class="divider"></div>
    <div class="contact-block">
      <h1 class="owner-name">Dorian Valcourt</h1>
      <p class="owner-title">Business Development Manager</p>
      <ul class="contact-list">
        <li class="contact-item">
          <svg class="contact-icon" viewBox="0 0 14 14"><rect x="3" y="1" width="8" height="12" rx="1.5" fill="none" stroke="#222326" stroke-width="1.3"/></svg>
          +64 (0) 22 4871 659
        </li>
        <li class="contact-item">
          <svg class="contact-icon" viewBox="0 0 14 14"><rect x="1" y="3" width="12" height="8" fill="#2a3b97"/><path d="M1 3 L7 8 L13 3" fill="none" stroke="#f3f3f3" stroke-width="1.2"/></svg>
          dorianv@r7mmeridian.nz
        </li>
        <li class="contact-item">
          <svg class="contact-icon" viewBox="0 0 14 14"><circle cx="7" cy="7" r="6" fill="#2a3b97"/><path d="M1 7 H13 M7 1 V13 M7 1 C3.5 4 3.5 10 7 13 M7 1 C10.5 4 10.5 10 7 13" fill="none" stroke="#f3f3f3" stroke-width="0.8"/></svg>
          www.r7mmeridian.nz
        </li>
      </ul>
    </div>
  </section>
</body>
</html>
```